Corporate Company Needs 3-series Flyer Template for Print

Flyer Contest Brief - We need a series of 3 templates to market and communicate our company’s leadership development program, using our corporate design elements. All 3 templates should have similar style, color, and elements --- but be noticeably different.

Template #1 – We need one template to communicate the Program Overview. It will include sections such as: learning objectives, descriptions about the online classes, a summary of required project, and the goals and purpose of the program

Template #2 – We need one template to communicate the details of an “Opening Event”. This template should include sections such as: Event location, event time, flight and hotel recommendations, event agenda, etc.

Template #3 - We need one template to communicate the details of an “Closing/Graduation Event”. This template should include sections such as: Event location, event time, flight and hotel recommendations, event agenda, etc.

Usage: We will edit and use the flyers to communicate our program, update information in the flyer and email the flyer to participants with each new class.

Our corporate design elements: Please refer to the attached PowerPoint file that includes a logo for the program, called CLIMB, and the purple brand color used for the program.

Size: Each template should be 8.5 x 11 inches

Look And Feel: Bold, Modern, Professional

File Type: Because I will edit, I need the flyer to be created in Microsoft Publisher or PowerPoint.

About the Program: The program is called CLIMB. It stands for Collaborative Learning In Modern Business. This program is a high profile executive leadership course that lasts for approximately 5 months. Participants attend a live opening event and a live closing / graduation event. Over the course of 5 months the coursework includes: attending online classrooms, regional meetings, e-Learning classes, and manage a project. It is an exclusive program for high profile professional speakers, and it's important for the flyer to be engaging, professional, and clean.

I will need to be able to make small edits back and forth with the successful designer in order to get it just-right. This may only be possibly 2-3 rounds of edits.

Reason: I'm extending the deadline. A few designers have requested this. Thank you.

Target Market(s)

Professional Executive Leaders in my company. Company is Brindlewood Group, USA.

Industry/Entity Type

It Company

Colors
6b449b
0792cd
00a990
add136
fbf289
f04a50

Requirements
Must have
• I must be able to edit all elements of the 3 templates. Therefore, it must be in PowerPoint or Publisher. The designs must use our logo and our purple brand color.
Nice to have
• It would be nice if the designer used the colors provided in the PowerPoint file. It would be nice to see icons used creatively.
Should not have
• Design should not have fancy text or use pictures of people.

```html
<!DOCTYPE html>
<html lang="en">
<head>
<meta charset="utf-8">
<title>CLIMB Opening Event Flyer</title>
<link rel="stylesheet" href="https://fonts.googleapis.com/css2?family=Ubuntu:wght@300;400;500;700&display=swap">
<style>
  :root {
    --page-bg: #e9e8e6;
    --paper: #ffffff;
    --brand-purple: #7a2f91;
    --deep-purple: #4a2a6e;
    --band-grey: #c9c8cc;
    --ink: #1c1c1c;
    --ink-soft: #4a4a4a;
    --dot-lilac: #c9a6d8;
    --on-purple: #ffffff;
    --on-purple-soft: #efe3f5;
  }
  * { box-sizing: border-box; margin: 0; padding: 0; }
  html, body { width: 1200px; height: 1200px; overflow: hidden; }
  body { background: var(--page-bg); font-family: "Ubuntu", sans-serif; }

  .flyer {
    position: absolute; left: 160px; top: 30px;
    width: 880px; height: 1139px;
    background: var(--paper);
    overflow: hidden;
    box-shadow: 0 2px 10px rgba(0,0,0,.12);
  }
  .dot-field {
    position: absolute; left: 0; top: 0; width: 100%; height: 340px;
    background: linear-gradient(180deg, rgba(201,166,216,.55) 0%, rgba(201,166,216,.25) 55%, rgba(255,255,255,0) 100%);
  }
  .faint-mark {
    position: absolute; left: 40px; top: 300px; width: 420px; height: 380px;
    background: #f1f1f1;
  }
  .waves { position: absolute; left: 0; top: 0; width: 880px; height: 1139px; }

  .brand {
    position: absolute; left: 0; width: 100%; top: 200px;
    text-align: center;
  }
  .brand-lockup { display: inline-flex; align-items: center; gap: 16px; }
  .brand-square { width: 62px; height: 62px; background: var(--brand-purple); }
  .brand-name { font-size: 112px; font-weight: 500; color: var(--ink); line-height: 1; letter-spacing: -2px; }
  .brand-expansion {
    margin-top: 10px; font-size: 13px; font-weight: 400;
    color: var(--brand-purple); letter-spacing: .5px; text-transform: uppercase;
  }

  .event-when { position: absolute; left: 0; width: 100%; top: 395px; text-align: center; }
  .event-date { font-size: 48px; font-weight: 500; color: var(--brand-purple); }
  .event-time { font-size: 38px; font-weight: 300; color: var(--ink-soft); margin-top: 2px; }
  .divider {
    width: 380px; height: 1px; margin: 18px auto 0;
    background: linear-gradient(90deg, rgba(122,47,145,0), var(--brand-purple), rgba(122,47,145,0));
  }
  .event-location { font-size: 34px; font-weight: 400; color: var(--ink); margin-top: 18px; }

  .details {
    position: absolute; left: 40px; right: 40px; top: 712px;
    text-align: center; color: var(--on-purple);
  }
  .section-title { font-size: 30px; font-weight: 400; }
  .flight-list { list-style: none; margin-top: 10px; font-size: 15px; font-weight: 300; line-height: 25px; color: var(--on-purple-soft); }
  .flight-list svg { width: 11px; height: 11px; margin-right: 6px; vertical-align: -1px; }
  .hotel-title { margin-top: 10px; }
  .hotel-text { font-size: 15px; font-weight: 300; margin-top: 8px; color: var(--on-purple-soft); }
  .agenda-title { font-size: 32px; font-weight: 700; margin-top: 18px; }
  .agenda-text { font-size: 15px; font-weight: 300; line-height: 23px; margin-top: 10px; color: var(--on-purple-soft); }
  .agenda-text strong { font-weight: 500; color: var(--on-purple); }
</style>
</head>
<body>
  <main class="flyer">
    <div class="dot-field" role="img" aria-label="Decorative pattern of small lilac dots fading downward"></div>
    <div class="faint-mark" aria-hidden="true"></div>

    <svg class="waves" viewBox="0 0 880 1139" aria-hidden="true">
      <defs>
        <linearGradient id="purple-fill" x1="0" y1="0" x2="0" y2="1">
          <stop offset="0" stop-color="#6e3d96"/>
          <stop offset="1" stop-color="#8b2f96"/>
        </linearGradient>
      </defs>
      <path d="M0 790 C250 560 600 545 880 760 L880 1139 L0 1139 Z" fill="var(--band-grey)"/>
      <path d="M0 808 C250 578 600 563 880 778 L880 1139 L0 1139 Z" fill="var(--deep-purple)"/>
      <path d="M0 880 C250 650 600 650 880 850 L880 1139 L0 1139 Z" fill="url(#purple-fill)"/>
    </svg>

    <header class="brand">
      <div class="brand-lockup">
        <span class="brand-square"></span>
        <span class="brand-name">climb</span>
      </div>
      <p class="brand-expansion">Collaborative Learning In Modern Business</p>
    </header>

    <section class="event-when">
      <p class="event-date">January 15th, 2017</p>
      <p class="event-time">10 am</p>
      <div class="divider"></div>
      <p class="event-location">Event location Lorem Ipsum</p>
    </section>

    <section class="details">
      <h2 class="section-title">Flight</h2>
      <ul class="flight-list">
        <li><svg viewBox="0 0 12 12"><path d="M2 10 L10 2 M4 2 H10 V8" stroke="#fff" stroke-width="2.2" fill="none"/></svg>Lorem Ipsum is simply dummy text of the printing and typesetting industry.</li>
        <li><svg viewBox="0 0 12 12"><path d="M2 10 L10 2 M4 2 H10 V8" stroke="#fff" stroke-width="2.2" fill="none"/></svg>Lorem Ipsum has been the industry's standard dummy text ever since the 1500s.</li>
        <li><svg viewBox="0 0 12 12"><path d="M2 10 L10 2 M4 2 H10 V8" stroke="#fff" stroke-width="2.2" fill="none"/></svg>It was popularised in the 1960s.</li>
        <li><svg viewBox="0 0 12 12"><path d="M2 10 L10 2 M4 2 H10 V8" stroke="#fff" stroke-width="2.2" fill="none"/></svg>also the leap into electronic typesetting, remaining essentially unchanged.</li>
      </ul>
      <h2 class="section-title hotel-title">Hotel</h2>
      <p class="hotel-text">Lorem Ipsum is simply dummy text of the printing and typesetting industry.</p>
      <h2 class="agenda-title">Event Agenda</h2>
      <p class="agenda-text"><strong>CLIMB</strong> is a multi-site manager development program designed to build a bench of multi-site managers consistent with the growth of the business and expected rate of labor turnover. Participants in <strong>CLIMB</strong> have the opportunity to meet, network and collaborate with colleagues representing the spectrum of sectors and business lines in Brindlewood Group.</p>
      <p class="agenda-text">The <strong>CLIMB</strong> program consists of a live kickoff event, self-directed learning, virtual classroom experiences, a project and a closing</p>
    </section>
  </main>
</body>
</html>
```